Website For Custom Home Builder

-Very elegant and simple design as I am a high end custom home builder.
-I build homes $2 million to $10 million range so the website needs to reflect the level of home that I build.
-Attached are photos of homes I have built to use as well as my logo.
-I need final design to be in layered format so my local guy can edit if he needs to.

3 Page Design
1. HomePage:
-logo, some photos,
-“Building beautiful custom homes in Indianapolis for over 20 years”
2. AboutPage:
-Wade Holloran has been building stunning custom homes in the Indianpolis area for over 20 years. As a small boutique building company we only build a handful of homes a year in order to offer our clients the personal attention that their homes deserve. It's this attention to detail that makes our client experience and final product something special and unique.
- family photo
3. ContactPage:
-office photo
-317-552-7190
-wade@whcrafted.com
-415 North Fernmill Rd, Suite 308, Carmel IN 46033

Target Market(s)

Very high end clients looking to build $2 million to $10 million homes.

Industry/Entity Type

Residential high end custom home builder/construction

Coding

Coded - Design and coding required

Number of Pages Required

3 page

Requirements
Must have
• Very simple and elegant design that represents the high end homes that I build.
Nice to have
Should not have
• Should NOT have a lot of clutter or be a very busy page from a design perspective.

```html
<!DOCTYPE html>
<html lang="en">
<head>
<meta charset="utf-8">
<title>Wade Holloran — Custom Homes</title>
<link rel="stylesheet" href="https://fonts.googleapis.com/css2?family=Poppins:wght@200;300;400;500;600&display=swap">
<style>
:root{
  --ink:#000000;
  --white:#ffffff;
  --soft:#d9d9d9;
  --muted:#9a9a9a;
  --accent:#f0a12e;
  --line:rgba(255,255,255,.35);
}
*{box-sizing:border-box;margin:0;padding:0}
html,body{width:1200px;height:2208px;overflow:hidden;background:var(--ink);font-family:"Poppins",sans-serif;color:var(--white)}
.page{position:relative;width:1200px;height:2208px}
.abs{position:absolute}

/* hero */
.hero{position:absolute;left:0;top:0;width:1200px;height:754px;
  background:linear-gradient(180deg,#2f2a25 0%,#4a3a2c 22%,#3a3128 45%,#2a2620 68%,#2b2a26 85%,#3b3a36 100%)}
.brand{position:absolute;font-weight:300;letter-spacing:.02em;color:var(--white);white-space:nowrap}
.hero .brand{left:100px;top:66px;font-size:22px}
.nav{position:absolute;top:68px;left:735px;display:flex;gap:0;font-size:13px;font-weight:500;letter-spacing:.06em}
.nav a{color:var(--white);text-decoration:none;position:absolute;white-space:nowrap}
.nav a.active{padding-bottom:6px;border-bottom:1px solid var(--accent)}
.hero-title{position:absolute;left:0;top:322px;width:1200px;text-align:center;font-weight:200;font-size:47px;line-height:60px;text-transform:uppercase}
.hero-title .hl{color:var(--accent)}
.btn{position:absolute;border:1px solid var(--white);display:flex;align-items:center;justify-content:center;font-size:11px;font-weight:600;letter-spacing:.12em;color:var(--white);text-decoration:none}
.hero .btn{left:514px;top:546px;width:171px;height:47px}
.arrow{position:absolute;top:388px;width:53px;height:53px}

/* feature */
.feature{position:absolute;left:0;top:754px;width:1200px;height:587px;background:var(--ink)}
.feature-photo{position:absolute;left:100px;top:109px;width:563px;height:375px;
  background:linear-gradient(180deg,#6b5a45 0%,#a37a45 30%,#c89a5c 52%,#8a7765 66%,#1f4fb0 80%,#0a2f8a 100%)}
.feature-title{position:absolute;left:704px;top:126px;font-size:41px;font-weight:300;line-height:49px}
.feature-text{position:absolute;left:706px;top:243px;width:400px;font-size:14.3px;line-height:25px;font-weight:400}
.progress{position:absolute;left:706px;top:405px;display:flex;gap:2px}
.progress span{display:block;width:88px;height:1px;background:var(--white)}
.progress span.on{height:5px;margin-top:-2px}

/* consultation */
.consult{position:absolute;left:0;top:1341px;width:1200px;height:418px;
  background:linear-gradient(90deg,#4a4a48 0%,#5a5a57 35%,#6d6c68 60%,#5e5d5a 100%)}
.consult-title{position:absolute;left:100px;top:92px;font-size:40px;font-weight:300;line-height:48px}
.consult .btn{left:100px;top:273px;width:170px;height:47px}

/* footer */
.footer{position:absolute;left:0;top:1759px;width:1200px;height:449px;background:var(--ink)}
.footer .brand{left:100px;top:148px;font-size:28px}
.col-title{position:absolute;top:78px;font-size:26px;font-weight:300}
.links{position:absolute;left:400px;top:141px;list-style:none;font-size:14px;font-weight:300}
.links li{height:40px}
.contact-item{position:absolute;left:663px;display:flex;align-items:flex-start;gap:14px;font-size:14px;font-weight:300;line-height:25px}
.icon-ring{width:32px;height:32px;border:1px solid #555;border-radius:50%;display:flex;align-items:center;justify-content:center;flex:none}
.mail{color:var(--accent)}
.socials{position:absolute;left:921px;top:142px;display:flex;gap:13px}
.socials span{width:31px;height:31px;border:1px solid #555;border-radius:50%}
.legal{position:absolute;left:0;top:403px;width:1200px;border-top:1px solid #333;text-align:center;font-size:10px;color:var(--muted);padding-top:14px}
</style>
</head>
<body>
<div class="page">

  <header class="hero" role="img" aria-label="Photo of a stone and timber custom home at dusk with lit windows">
    <div class="brand">Wade Holloran</div>
    <nav class="nav">
      <a class="active" style="left:0">HOME</a>
      <a style="left:82px">ABOUT US</a>
      <a style="left:193px">GALLERY</a>
      <a style="left:294px">CONTACT</a>
    </nav>
    <svg class="arrow" style="left:46px" viewBox="0 0 53 53"><circle cx="26.5" cy="26.5" r="26" fill="none" stroke="#fff" stroke-width="1"/><path d="M37 26.5H16M24 18.5l-8 8 8 8" fill="none" stroke="#fff" stroke-width="1.5"/></svg>
    <svg class="arrow" style="left:1099px" viewBox="0 0 53 53"><circle cx="26.5" cy="26.5" r="26" fill="none" stroke="#fff" stroke-width="1"/><path d="M16 26.5h21M29 18.5l8 8-8 8" fill="none" stroke="#fff" stroke-width="1.5"/></svg>
    <h1 class="hero-title">Building beautiful custom<br>homes in <span class="hl">Indianapolis</span> for<br>over 20 years</h1>
    <a class="btn">CONTACT NOW</a>
  </header>

  <section class="feature">
    <div class="feature-photo" role="img" aria-label="Photo of a luxury home's rear terrace with a lit blue pool at dusk"></div>
    <h2 class="feature-title">Custom Luxury<br>Homes &amp; Desings</h2>
    <p class="feature-text">Lorem Ipsum is simply dummy text of the printing and typesetting industry. Lorem Ipsum has been the in-dustry's standard dummy text ever since the 1500s, when an unknown printer took a galley of type and scrambled it to make a type specimen book.</p>
    <div class="progress"><span class="on"></span><span></span><span></span><span></span></div>
  </section>

  <section class="consult" role="img" aria-label="Photo of a bright living room with fireplace, grey armchairs and large windows">
    <h2 class="consult-title">Book Your Free<br>Consultation. Your Luxury<br>Home Awaits You!</h2>
    <a class="btn">CONTACT NOW</a>
  </section>

  <footer class="footer">
    <div class="brand">Wade Holloran</div>

    <h3 class="col-title" style="left:399px">Quick Links</h3>
    <ul class="links">
      <li>Home</li><li>About us</li><li>Gallery</li><li>Contact</li>
    </ul>

    <h3 class="col-title" style="left:665px;top:76px">Contact Us</h3>
    <div class="contact-item" style="top:137px">
      <span class="icon-ring"><svg width="12" height="14" viewBox="0 0 12 14"><path d="M6 0a5 5 0 0 0-5 5c0 3.6 5 9 5 9s5-5.4 5-9a5 5 0 0 0-5-5zm0 7a2 2 0 1 1 0-4 2 2 0 0 1 0 4z" fill="#fff"/></svg></span>
      <span>415 North Fernmill Rd,<br>Suite 308,<br>Carmel IN 46033</span>
    </div>
    <div class="contact-item" style="top:232px">
      <span class="icon-ring"><svg width="13" height="13" viewBox="0 0 13 13"><path d="M3 .5l2 3-1.3 1.4a8 8 0 0 0 4.4 4.4L9.5 8l3 2-1 2.5C5.8 12.8.2 7.2.5 1.5z" fill="#fff"/></svg></span>
      <span style="padding-top:3px">317-552-7190</span>
    </div>
    <div class="contact-item" style="top:283px">
      <span class="icon-ring"><svg width="12" height="9" viewBox="0 0 12 9"><rect width="12" height="9" fill="#fff"/><path d="M0 0l6 5 6-5" fill="none" stroke="#000" stroke-width="1"/></svg></span>
      <span class="mail" style="padding-top:3px">wade@whcrafted.com</span>
    </div>

    <h3 class="col-title" style="left:927px">Social Media</h3>
    <div class="socials"><span></span><span></span><span></span><span></span></div>

    <div class="legal">© 2023 whcrafted. All rights reserved.</div>
  </footer>

</div>
</body>
</html>
```